Powepoint template for an investment group

Need high end clear clean concise creative luxurious

Have royal clients
High end/billionaire investors

Using ross gold logo can be creative
Must habe page numbers
Logo preference header top right
Page number footer bottom right

The first page of the ppt maybe a big block of dark grey and ulvo investment group written on the front page in rose gold

Target Market(s)

Investors at a high level

Requirements
Must have
• Luxury feel

```html
<!DOCTYPE html>
<html lang="en">
<head>
<meta charset="utf-8">
<title>Ulvo Investment Group – Presentation Template</title>
<link rel="stylesheet" href="https://fonts.googleapis.com/css2?family=Montserrat:wght@300;400;500;600;700&family=Source+Sans+3:wght@400;600&family=Libre+Baskerville&display=swap">
<style>
  :root{
    --canvas:#e1e1e1;
    --white:#ffffff;
    --ink:#0a0a0a;
    --text:#1d1d1d;
    --rose:#d5a096;
    --rose-light:#ecd0cb;
    --grey-bar:#bdbdbf;
    --navy:#34405a;
    --grid:#c9d4e3;
    --axis:#b7c6da;
  }
  *{margin:0;padding:0;box-sizing:border-box}
  html,body{width:1200px;height:1155px;overflow:hidden;background:var(--canvas)}
  body{position:relative;font-family:"Montserrat",sans-serif;color:var(--text)}
  .slide{position:absolute;width:514px;height:289px;background:var(--white);overflow:hidden}
  .slide > svg{position:absolute;left:0;top:0;width:514px;height:289px}
  .slide--cover{left:66px;top:95px}
  .slide--about{left:619px;top:95px}
  .slide--chart{left:66px;top:431px}
  .slide--growth{left:619px;top:431px}
  .slide--services{left:66px;top:770px}
  .slide--closing{left:619px;top:770px}

  .page-number{position:absolute;right:10px;bottom:7px;font-family:"Montserrat",sans-serif;font-size:7px;font-weight:500;letter-spacing:.5px;color:#6a6a6a}
  .page-number--light{color:var(--white)}
  .page-number--rose{color:var(--rose)}

  .brand{position:absolute;text-align:center;font-family:"Montserrat",sans-serif}
  .brand__name{display:block;font-size:30px;font-weight:500;letter-spacing:2px;line-height:1;color:var(--rose)}
  .brand__tag{display:block;font-size:12px;font-weight:300;letter-spacing:.8px;margin-top:9px;color:var(--white)}
  .slide--cover .brand{left:312px;top:50px;width:186px}
  .slide--closing .brand{left:336px;top:72px;width:170px}

  .web{position:absolute;left:386px;top:255px;display:flex;align-items:center;gap:7px;color:#e8e8e8;font-family:"Libre Baskerville",serif;font-size:7.5px}
  .web__dot{width:11px;height:11px;border:1px solid var(--rose);border-radius:50%;position:relative}
  .web__dot::after{content:"";position:absolute;left:3px;top:2.5px;border-left:4px solid var(--rose);border-top:2px solid transparent;border-bottom:2px solid transparent;transform:rotate(-40deg)}

  .about__copy{position:absolute;left:39px;top:20px;width:370px;font-size:9.9px;line-height:15.2px;color:var(--text)}
  .about__copy p + p{margin-top:17px}
  .steps{position:absolute;left:39px;top:240px;display:flex}
  .step{width:55px;text-align:center;font-size:6.2px;font-weight:600;color:var(--text)}
  .step small{display:block;font-size:4.2px;font-weight:400;line-height:5px;margin-top:1px}
  .step-label{font-family:"Montserrat",sans-serif;font-size:6.6px;font-weight:700;fill:var(--text);text-anchor:middle}

  .chart__title{position:absolute;left:0;width:320px;top:30px;text-align:center;font-size:14px;font-weight:700;color:var(--ink)}
  .axis-label{font-family:"Montserrat",sans-serif;font-size:8.5px;font-weight:600;fill:var(--ink)}
  .cat-label{font-family:"Montserrat",sans-serif;font-size:8.3px;font-weight:600;fill:var(--ink);text-anchor:middle}
  .chart__note{position:absolute;left:24px;top:208px;width:360px;font-size:10.2px;line-height:15.3px}

  .growth__panel{position:absolute;left:0;width:187px;padding:0 29px;font-size:9px;font-weight:300;line-height:12.8px;text-align:justify;color:var(--white)}
  .growth__panel--rose{top:0;height:173px;background:var(--rose);padding-top:17px}
  .growth__panel--ink{top:173px;height:116px;background:var(--ink);padding-top:14px}
  .tick{font-family:"Montserrat",sans-serif;font-size:5.5px;fill:#aab8cc;text-anchor:middle}
  .flag{font-family:"Montserrat",sans-serif;font-size:8.4px;font-weight:600;fill:var(--white);text-anchor:middle}

  .services{font-family:"Source Sans 3",sans-serif}
  .services__title{position:absolute;left:31px;top:20px;font-size:20px;font-weight:400;color:var(--ink)}
  .services__sub{position:absolute;left:32px;top:48px;font-size:11px;padding-left:4px;border-left:1.5px solid var(--rose);line-height:12px;color:var(--ink)}
  .services__intro{position:absolute;left:32px;top:70px;width:451px;font-size:8.1px;line-height:10.5px;text-align:justify;color:var(--ink)}
  .service{position:absolute;top:152px;width:100px;text-align:center}
  .service__icon{display:block;margin:0 auto;width:40px;height:36px}
  .service__name{display:block;margin-top:8px;font-size:17.5px;line-height:18px;color:var(--ink);white-space:nowrap}
  .service__text{display:block;margin-top:7px;font-size:7.8px;line-height:9px;color:#333}
</style>
</head>
<body>

<!-- Cover -->
<section class="slide slide--cover">
  <svg viewBox="0 0 514 289">
    <defs>
      <linearGradient id="coverPhoto" x1="0" y1="0" x2="1" y2="1">
        <stop offset="0" stop-color="#b9c8c4"/>
        <stop offset=".45" stop-color="#d9b2a8"/>
        <stop offset="1" stop-color="#c59489"/>
      </linearGradient>
    </defs>
    <polygon role="img" aria-label="Photo: hands writing notes beside a laptop on a desk, rose-tinted" points="0,0 323,0 264,95 386,289 0,289" fill="url(#coverPhoto)"/>
    <polygon points="205,0 323,0 264,95 386,289 135,289" fill="var(--rose)" opacity=".35"/>
    <polygon points="323,0 514,0 514,289 386,289 264,95" fill="var(--ink)"/>
  </svg>
  <div class="brand"><span class="brand__name">ULVO</span><span class="brand__tag">Investment Group</span></div>
  <div class="web"><span class="web__dot"></span>www.ulvogroup.example</div>
  <span class="page-number page-number--rose">01</span>
</section>

<!-- About -->
<section class="slide slide--about">
  <svg viewBox="0 0 514 289">
    <defs>
      <linearGradient id="aboutPhoto" x1="1" y1="0" x2="0" y2="1">
        <stop offset="0" stop-color="#c9d6ea"/>
        <stop offset=".55" stop-color="#e7e3e3"/>
        <stop offset="1" stop-color="#e8b596"/>
      </linearGradient>
    </defs>
    <polygon role="img" aria-label="Photo: hand pointing at charts on a tablet" points="514,0 514,289 329,289" fill="url(#aboutPhoto)"/>

    <g class="rings">
      <path d="M33,198 A34,34 0 0 1 101,198 Z" fill="var(--ink)"/>
      <path d="M33,198 A34,34 0 0 0 101,198 Z" fill="var(--rose)"/>
      <path d="M88,198 A34,34 0 0 1 156,198 Z" fill="var(--rose)"/>
      <path d="M88,198 A34,34 0 0 0 156,198 Z" fill="var(--ink)"/>
      <path d="M142,198 A34,34 0 0 1 210,198 Z" fill="var(--ink)"/>
      <path d="M142,198 A34,34 0 0 0 210,198 Z" fill="var(--rose)"/>
      <path d="M197,198 A34,34 0 0 1 265,198 Z" fill="var(--rose)"/>
      <path d="M197,198 A34,34 0 0 0 265,198 Z" fill="var(--ink)"/>
      <path d="M251,198 A34,34 0 0 1 319,198 Z" fill="var(--ink)"/>
      <path d="M251,198 A34,34 0 0 0 319,198 Z" fill="var(--rose)"/>
      <g fill="var(--white)">
        <circle cx="67" cy="198" r="23"/><circle cx="122" cy="198" r="23"/>
        <circle cx="176" cy="198" r="23"/><circle cx="231" cy="198" r="23"/>
        <circle cx="285" cy="198" r="23"/>
      </g>
      <g fill="none" stroke="#9fb0c8" stroke-width=".8">
        <path d="M95,226 Q107,235 118,228"/><path d="M204,226 Q216,235 227,228"/>
        <path d="M150,170 Q160,162 170,168"/><path d="M258,170 Q268,162 278,168"/>
      </g>
      <g fill="none" stroke="#7e93b4" stroke-width="1">
        <circle cx="68" cy="186" r="3.2"/><line x1="65.8" y1="188.3" x2="63.5" y2="190.6"/>
        <path d="M174,183 h4 M175,183 v3 l-2.5,5 h7 l-2.5,-5 v-3"/>
        <circle cx="231" cy="183.5" r="1.4"/><path d="M231,185 v7 M228,187 h6 M227.5,189.5 q3.5,3 7,0"/>
        <path d="M283,191 l1,-3 5,-5 2,2 -5,5 z"/>
      </g>
      <path d="M119.5,184 q-2.5,3 0,6 h5 q2.5,-3 0,-6 l1.5,-2 h-8 z" fill="#7e93b4"/>
      <text x="122" y="189" font-size="3.5" fill="#fff" text-anchor="middle" font-family="Montserrat,sans-serif">$</text>
      <text x="67" y="200" class="step-label">Step</text><text x="67" y="207" class="step-label">01</text>
      <text x="122" y="200" class="step-label">Step</text><text x="122" y="207" class="step-label">02</text>
      <text x="176" y="200" class="step-label">Step</text><text x="176" y="207" class="step-label">03</text>
      <text x="231" y="200" class="step-label">Step</text><text x="231" y="207" class="step-label">04</text>
      <text x="285" y="200" class="step-label">Step</text><text x="285" y="207" class="step-label">05</text>
    </g>
  </svg>
  <div class="about__copy">
    <p>is a leading private investor and business accelerator that leverages the experience, insights, and resources of its founder,<br>Mr. Daniel R. Okoye, an accomplished entrepreneur and investor.</p>
    <p>Harbourne Capital has been investing its own capital since 1998 and has had a prestigious track record generating over $2 Billion in enterprise value across various industries including financial services, software, biotechnology, advanced manufacturing, and alternative energy.</p>
  </div>
  <div class="steps">
    <div class="step">Title One<small>Nam pretium turpis et arcu. Duis arcu</small></div>
    <div class="step">Title Two<small>Nam pretium turpis et arcu. Duis arcu</small></div>
    <div class="step">Title Three<small>Nam pretium turpis et arcu. Duis arcu</small></div>
    <div class="step">Title Four<small>Nam pretium turpis et arcu. Duis arcu</small></div>
    <div class="step">Title Five<small>Nam pretium turpis et arcu. Duis arcu</small></div>
  </div>
  <span class="page-number">02</span>
</section>

<!-- Bar chart -->
<section class="slide slide--chart">
  <svg viewBox="0 0 514 289">
    <g stroke="#e2e2e2" stroke-width=".7">
      <line x1="31" y1="56" x2="298" y2="56"/><line x1="31" y1="76" x2="298" y2="76"/>
      <line x1="31" y1="96" x2="298" y2="96"/><line x1="31" y1="116" x2="298" y2="116"/>
      <line x1="31" y1="137" x2="298" y2="137"/><line x1="31" y1="157" x2="298" y2="157"/>
      <line x1="31" y1="177" x2="298" y2="177"/>
    </g>
    <text class="axis-label" x="21" y="59">6</text><text class="axis-label" x="21" y="79">5</text>
    <text class="axis-label" x="21" y="99">4</text><text class="axis-label" x="21" y="119">3</text>
    <text class="axis-label" x="21" y="140">2</text><text class="axis-label" x="21" y="160">1</text>
    <text class="axis-label" x="21" y="180">0</text>
    <rect x="56" y="91" width="15" height="86" fill="var(--rose)"/>
    <rect x="78" y="120" width="15" height="57" fill="var(--ink)"/>
    <rect x="100" y="141" width="14" height="36" fill="var(--grey-bar)"/>
    <rect x="149" y="128" width="14" height="49" fill="var(--rose)"/>
    <rect x="170" y="91" width="15" height="86" fill="var(--ink)"/>
    <rect x="192" y="141" width="15" height="36" fill="var(--grey-bar)"/>
    <rect x="242" y="106" width="14" height="71" fill="var(--rose)"/>
    <rect x="263" y="92" width="15" height="85" fill="var(--ink)"/>
    <rect x="284" y="120" width="15" height="57" fill="var(--grey-bar)"/>
    <text class="cat-label" x="83" y="191">Category 1</text>
    <text class="cat-label" x="176" y="191">Category 2</text>
    <text class="cat-label" x="269" y="191">Category 3</text>
    <polygon points="514,95 514,289 390,289" fill="var(--rose)"/>
  </svg>
  <h2 class="chart__title">ULVO CHART</h2>
  <p class="chart__note">The entrepreneurial heritage and innovative spirit of the firm allows it to take unconventional and creative approaches to investing, that are often contrarian and sometimes pioneering.</p>
  <span class="page-number page-number--light">03</span>
</section>

<!-- Line chart -->
<section class="slide slide--growth">
  <div class="growth__panel growth__panel--rose">Ulvo Investment Group has been investing its own capital since 1998 and has had a prestigious track record generating over $2 Billion in enterprise value across various industries including financial services, software, biotechnology, advanced manufacturing, and alternative energy.</div>
  <div class="growth__panel growth__panel--ink">Ulvo Investment Group has been investing its own capital since 1998 and has had a prestigious track record generating over $2 Billion in</div>
  <svg viewBox="0 0 514 289">
    <g stroke="var(--grid)" stroke-width=".6">
      <line x1="253.5" y1="74" x2="253.5" y2="215"/><line x1="273" y1="74" x2="273" y2="215"/>
      <line x1="292.6" y1="74" x2="292.6" y2="215"/><line x1="312" y1="74" x2="312" y2="215"/>
      <line x1="331.7" y1="74" x2="331.7" y2="215"/><line x1="351.3" y1="74" x2="351.3" y2="215"/>
      <line x1="370.9" y1="74" x2="370.9" y2="215"/><line x1="390.4" y1="74" x2="390.4" y2="215"/>
      <line x1="410" y1="74" x2="410" y2="215"/><line x1="429.5" y1="74" x2="429.5" y2="215"/>
      <line x1="449.1" y1="74" x2="449.1" y2="215"/>
      <line x1="234" y1="94.4" x2="468" y2="94.4"/><line x1="234" y1="114.5" x2="468" y2="114.5"/>
      <line x1="234" y1="134.6" x2="468" y2="134.6"/><line x1="234" y1="154.7" x2="468" y2="154.7"/>
      <line x1="234" y1="174.8" x2="468" y2="174.8"/><line x1="234" y1="194.9" x2="468" y2="194.9"/>
    </g>
    <g stroke="var(--axis)" stroke-width="1.6">
      <line x1="234" y1="74" x2="234" y2="216"/><line x1="233" y1="215" x2="468" y2="215"/>
    </g>
    <text class="tick" x="228" y="97">6</text><text class="tick" x="228" y="117">5</text>
    <text class="tick" x="228" y="137">4</text><text class="tick" x="228" y="157">3</text>
    <text class="tick" x="228" y="177">2</text><text class="tick" x="228" y="197">1</text>
    <text class="tick" x="228" y="224">0</text>
    <text class="tick" x="253.5" y="224">1</text><text class="tick" x="273" y="224">2</text>
    <text class="tick" x="292.6" y="224">3</text><text class="tick" x="312" y="224">4</text>
    <text class="tick" x="331.7" y="224">5</text><text class="tick" x="351.3" y="224">6</text>
    <text class="tick" x="370.9" y="224">7</text><text class="tick" x="390.4" y="224">8</text>
    <text class="tick" x="410" y="224">9</text><text class="tick" x="429.5" y="224">10</text>
    <text class="tick" x="449.1" y="224">11</text>
    <g fill="none" stroke-width="1.2">
      <path d="M234,215 C250,150 265,118 292.6,114.5 C330,110 345,96 370.9,98.4 C405,102 430,115 449.1,144.6" stroke="var(--navy)"/>
      <path d="M234,215 C252,165 265,136 292.6,134.6 C325,130 345,113 370.9,114.5 C400,116 420,115 449.1,104.5" stroke="#253048"/>
      <path d="M234,215 C252,175 265,148 292.6,142.6 C325,136 350,134 370.9,134.6 C395,136 405,147 420,142 C432,138 440,128 449.1,114.5" stroke="#4a5a78"/>
      <path d="M234,215 C250,185 265,160 292.6,154.7 C325,146 350,140 370.9,154.7 C390,168 400,183 420,174 C430,170 440,176 449.1,174.8" stroke="#c8877c"/>
      <path d="M234,215 C252,195 270,178 292.6,174.8 C330,168 345,185 370.9,186.9 C400,185 420,110 449.1,94.4" stroke="#eab1a8"/>
    </g>
    <circle cx="292.6" cy="114.5" r="2.6" fill="#7d8cab"/><circle cx="370.9" cy="98.4" r="2.6" fill="var(--navy)"/><circle cx="449.1" cy="144.6" r="2.6" fill="var(--navy)"/>
    <circle cx="292.6" cy="134.6" r="2.6" fill="#253048"/><circle cx="370.9" cy="114.5" r="2.6" fill="#253048"/><circle cx="449.1" cy="104.5" r="2.6" fill="#253048"/>
    <circle cx="292.6" cy="142.6" r="2.6" fill="#4a5a78"/><circle cx="370.9" cy="134.6" r="2.6" fill="#4a5a78"/><circle cx="449.1" cy="114.5" r="2.6" fill="#4a5a78"/>
    <circle cx="292.6" cy="154.7" r="2.6" fill="#c8877c"/><circle cx="370.9" cy="154.7" r="2.6" fill="#c8877c"/><circle cx="449.1" cy="174.8" r="2.6" fill="#c8877c"/>
    <circle cx="292.6" cy="174.8" r="2.6" fill="#eab1a8"/><circle cx="370.9" cy="186.9" r="2.6" fill="#eab1a8"/><circle cx="449.1" cy="94.4" r="2.6" fill="#f0b9b0"/>
    <rect x="295" y="83" width="54" height="16" fill="#e89d92"/>
    <polygon points="295,99 301,99 293,112" fill="#e89d92"/>
    <text class="flag" x="322" y="94">Title Value</text>
  </svg>
  <span class="page-number">04</span>
</section>

<!-- Services -->
<section class="slide slide--services services">
  <h2 class="services__title">Our Services</h2>
  <p class="services__sub">Best Solutions</p>
  <p class="services__intro">Lorem ipsum dolor sit amet, consectetuer adipiscing elit, sed diam nonummy nibh euismod tincidunt ut laoreet dolore magna aliquam erat volutpat. Ut wisi enim ad minim veniam, quis nostrud exerci tation ullamcorper suscipit lobortis nisl ut aliquip ex ea commodo consequat. Duis autem vel eum iriure dolor in hendrerit in vulputate velit esse molestie consequat, vel illum dolore eu feugiat nulla facilisis at vero eros et accumsan et iusto odio dignissim qui blandit praesent luptatum zzril delenit augue duis dolore te feugait nulla facilisi.</p>

  <div class="service" style="left:30px">
    <svg class="service__icon" viewBox="0 0 40 36"><polygon points="10,0 30,0 40,18 30,36 10,36 0,18" fill="var(--rose)"/>
      <circle cx="20" cy="18" r="9" fill="none" stroke="#fff" stroke-width="1.4"/><path d="M20,12 v6 l-4,3" fill="none" stroke="#fff" stroke-width="1.4"/></svg>
    <span class="service__name">Title Two</span>
    <span class="service__text">Pellentesque egestas, neque sit amet convallis pulvinar, justo nulla eleifend augue.</span>
  </div>
  <div class="service" style="left:148px">
    <svg class="service__icon" viewBox="0 0 40 36"><polygon points="10,0 30,0 40,18 30,36 10,36 0,18" fill="var(--rose)"/>
      <path d="M16,9 h8 M17.5,9 v7 l-5,10 h15 l-5,-10 v-7" fill="none" stroke="#fff" stroke-width="1.4"/><path d="M14.5,22 h11 l1.5,3 h-14 z" fill="#fff"/></svg>
    <span class="service__name">Title Three</span>
    <span class="service__text">Pellentesque egestas, neque sit amet convallis pulvinar, justo nulla eleifend augue.</span>
  </div>
  <div class="service" style="left:265px">
    <svg class="service__icon" viewBox="0 0 40 36"><polygon points="10,0 30,0 40,18 30,36 10,36 0,18" fill="var(--rose)"/>
      <path d="M16,9 h8 l-2,4 q6,4 6,10 q0,4 -4,4 h-8 q-4,0 -4,-4 q0,-6 6,-10 z" fill="#fff"/>
      <text x="20" y="25" font-size="8" text-anchor="middle" fill="var(--rose)" font-family="Source Sans 3,sans-serif" font-weight="600">$</text></svg>
    <span class="service__name">Title Four</span>
    <span class="service__text">Pellentesque egestas, neque sit amet convallis pulvinar, justo nulla eleifend augue.</span>
  </div>
  <div class="service" style="left:383px">
    <svg class="service__icon" viewBox="0 0 40 36"><polygon points="10,0 30,0 40,18 30,36 10,36 0,18" fill="var(--rose)"/>
      <g fill="none" stroke="#fff" stroke-width="1.3"><ellipse cx="20" cy="11" rx="7" ry="2.5"/><path d="M13,11 v14 q7,4 14,0 v-14 M13,16 q7,4 14,0 M13,20.5 q7,4 14,0"/></g></svg>
    <span class="service__name">Title Five</span>
    <span class="service__text">Pellentesque egestas, neque sit amet convallis pulvinar, justo nulla eleifend augue.</span>
  </div>
  <span class="page-number">05</span>
</section>

<!-- Closing -->
<section class="slide slide--closing">
  <svg viewBox="0 0 514 289">
    <defs>
      <linearGradient id="closingPhoto" x1="0" y1="0" x2="1" y2="1">
        <stop offset="0" stop-color="#1c2238"/>
        <stop offset=".45" stop-color="#6e6a74"/>
        <stop offset="1" stop-color="#d9d9e2"/>
      </linearGradient>
    </defs>
    <rect role="img" aria-label="Photo: business meeting with a pen, documents and a tablet over a city skyline" x="0" y="0" width="514" height="289" fill="url(#closingPhoto)"/>
    <polygon points="0,0 50,0 0,77" fill="#f4f4f6"/>
    <polygon points="50,0 167,0 0,260 0,77" fill="var(--rose-light)" opacity=".95"/>
    <polygon points="0,260 167,0 185,0 0,289" fill="#eeeeef" opacity=".5"/>
    <polygon points="344,0 357,0 299,105 286,105" fill="var(--ink)"/>
    <polygon points="370,0 378,0 284,146 276,146" fill="var(--rose-light)" opacity=".85"/>
    <polygon points="376,0 514,0 514,289 433,289 317,108" fill="var(--ink)"/>
  </svg>
  <div class="brand"><span class="brand__name">ULVO</span><span class="brand__tag">Investment Group</span></div>
  <span class="page-number page-number--rose">06</span>
</section>

</body>
</html>
```